Labelling for Ice cream products for Tullaby j's company

Hi
We are an Ice cream/Gelato company based in Birmingham UK. We need a design for packaging for some of our products. We are in need of packaging for round 400-500ml tubs and smaller round 125ml tubs (with lids). We also need a design for our plastic Ice Lolly wrappers (will provide dimensions if needed) this will be for a roll that is used on an Ice lolly wrapping machine, and also designs for stickers that will go on the top of 10 litre tubs and rectangular stickers for the side of 5 litre napoli pans. We currently have a diner that we sell, so a simple design for our inhouse scoop cups would also be good. The designs should be editable and allow for incorporation of pictures of different flavours. I will attach our logo, as we would like the design to be congruent with the logos colours. The design frostel wickham currently use is nice and though we want our packaging to be unique, something along those lines is were our minds are at t he moment. The designer is free to play with designs and make it look as high quality as they wish, though is must preferably look fun but not childish. A design that incorporates pascal colours would be nice but not essential so feel free to experiment.
So to conclude:
1. Design for 400-500ml round tubs with lids.
2. Design for Ice lolly wrappers.
3. Design for square labels for the top of 10 litre tubs and rectangular labes for the side of 5 litre napoli pans.
4. Basic design for in-house scoop cups.
I will upload our logo.
Many thanks and kind regards

Gerald

Colors
FFC000
F8CF3A
FAE287
FDF2CF
FEFAEE
EE7325
F08F49
F5BC92
FAE3D3
FDF4ED
EB3D1F
EC4F4E
F09395
F8D3D4
FCEDEE
E54698
E96AAD
F1A4CE
F9D9EA
FCEFF6
A7469A
B969AE
D3A5CF
EDDBEB
F8F0F9

Requirements
Nice to have
• It would also be nice to have a design for swirlino wrappers

```html
<!DOCTYPE html>
<html lang="en">
<head>
<meta charset="utf-8">
<title>Tullaby j's – Strawberry Packaging Range</title>
<link rel="stylesheet" href="https://fonts.googleapis.com/css2?family=Sniglet:wght@400;800&family=Nunito:wght@400;600;700;800&display=swap">
<style>
  :root{
    --bg-top:#9b2896;
    --bg-bottom:#680d64;
    --aqua:#a9e2e7;
    --cloud:#ffffff;
    --brand-ink:#6a1f6b;
    --label-pink:#ec4f8e;
    --badge-purple:#8e2f8f;
    --ink:#2a2a2a;
    --scoop-light:#f9d9ea;
    --scoop-mid:#f1a4ce;
    --lolly:#d8127c;
    --lolly-dark:#a80c60;
  }
  *{box-sizing:border-box;margin:0;padding:0}
  html,body{width:1200px;height:839px;overflow:hidden}
  body{
    position:relative;
    background:linear-gradient(180deg,var(--bg-top) 0%,var(--bg-bottom) 100%);
    font-family:"Nunito",sans-serif;
  }
  .panel{position:absolute;background:var(--aqua);overflow:hidden;border-radius:6px}
  .cloud{position:absolute;left:0;right:0;bottom:0;width:100%}
  .brand-name{
    font-family:"Nunito",sans-serif;font-weight:800;color:var(--brand-ink);
    white-space:nowrap;position:relative;z-index:2;letter-spacing:.01em;
  }
  .flavour{font-family:"Sniglet",sans-serif;font-weight:800;color:var(--label-pink);position:relative;z-index:2;line-height:1}
  .flavour small{display:block;font-size:.5em;font-weight:400;padding-left:40%}
  .badge{
    position:absolute;border-radius:50%;background:var(--badge-purple);color:#fff;
    display:flex;align-items:center;justify-content:center;text-align:center;
    font-family:"Nunito",sans-serif;font-weight:700;line-height:1.05;z-index:2;
  }
  .photo{position:absolute;z-index:1}

  /* master logo */
  .logo{position:absolute;left:70px;top:170px;color:#fff}
  .logo .brand-name{font-size:96px;color:#fff}

  /* lolly wrapper */
  .wrapper{left:722px;top:62px;width:148px;height:370px}
  .wrapper .brand-name{font-size:20px;text-align:center;margin-top:78px}
  .wrapper .flavour{font-size:17px;margin:26px 0 0 14px}
  .wrapper .flavour small{font-size:11px;padding:2px 0 0}
  .wrapper .badge{left:12px;top:228px;width:42px;height:42px;font-size:8.5px}
  .wrapper .photo{left:64px;top:196px;width:56px;height:146px;border-radius:26px 26px 6px 6px;
    background:linear-gradient(90deg,var(--lolly-dark),var(--lolly) 45%,var(--lolly-dark))}

  /* scoop cup band */
  .scoop-cup{left:916px;top:215px;width:236px;height:160px}
  .scoop-cup .brand-name{font-size:24px;text-align:center;margin-top:58px}

  /* 400ml tub front */
  .tub-front{left:92px;top:515px;width:246px;height:275px}
  .tub-front .brand-name{font-size:32px;text-align:center;margin-top:72px}
  .tub-front .flavour{font-size:22px;text-align:center;margin-top:86px}
  .tub-front .flavour small{font-size:12px;padding-left:50%}

  /* 400ml tub back */
  .tub-back{left:370px;top:515px;width:246px;height:275px}
  .tub-back .photo{left:0;top:28px;width:110px;height:225px;border-radius:0 60px 0 0;
    background:radial-gradient(circle at 55% 25%,var(--scoop-light),var(--scoop-mid) 45%,#d9a76a 70%,#c98f4c)}
  .tub-back .copy{position:absolute;left:120px;width:116px;font-size:10px;line-height:1.32;color:var(--ink);z-index:2}
  .tub-back .copy.top{top:30px}
  .tub-back .copy.bottom{top:205px}
  .tub-back .volume{position:absolute;left:62px;top:256px;font-size:10px;color:#777;z-index:2}

  /* 10 litre top sticker */
  .top-sticker{left:676px;top:462px;width:448px;height:205px}
  .top-sticker .brand-name{position:absolute;left:64px;top:52px;font-size:34px}
  .top-sticker .flavour{position:absolute;left:80px;top:138px;font-size:24px}
  .top-sticker .flavour small{font-size:13px;padding-left:0;margin-top:3px}
  .top-sticker .badge{left:255px;top:98px;width:50px;height:50px;font-size:9px}
  .top-sticker .photo{left:320px;top:30px;width:106px;height:140px;border-radius:50% 50% 40% 40%;
    background:radial-gradient(circle at 45% 40%,#fbe3ea,#f1a4ce 55%,#e96a8a 85%)}

  /* 5 litre side sticker */
  .side-sticker{left:700px;top:690px;width:410px;height:100px}
  .side-sticker .brand-name{position:absolute;left:110px;top:12px;font-size:24px}
  .side-sticker .flavour{position:absolute;left:40px;top:62px;font-size:16px}
  .side-sticker .flavour small{font-size:9px;padding-left:0}
  .side-sticker .badge{left:246px;top:46px;width:32px;height:32px;font-size:6px}
  .side-sticker .photo{left:300px;top:14px;width:80px;height:74px;border-radius:50%;
    background:radial-gradient(circle at 45% 40%,#fbe3ea,#f1a4ce 55%,#e96a8a 85%)}
</style>
</head>
<body>

<div class="logo"><span class="brand-name">Tullaby j's</span></div>

<section class="panel wrapper">
  <div class="brand-name">Tullaby j's</div>
  <div class="flavour">Strawberry<small>Ice Lolly</small></div>
  <div class="badge">100%<br>natural<br>flavor</div>
  <div class="photo" role="img" aria-label="Photo of a strawberry ice lolly on a wooden stick"></div>
  <svg class="cloud" viewBox="0 0 200 60" height="80" preserveAspectRatio="none" aria-hidden="true"><path fill="var(--cloud)" d="M0 60V25Q15 10 30 22Q45 5 65 18Q85 4 105 18Q125 6 140 20Q160 8 180 22Q192 14 200 20V60Z"/></svg>
</section>

<section class="panel scoop-cup">
  <div class="brand-name">Tullaby j's</div>
  <svg class="cloud" viewBox="0 0 200 60" height="50" preserveAspectRatio="none" aria-hidden="true"><path fill="var(--cloud)" d="M0 60V25Q15 10 30 22Q45 5 65 18Q85 4 105 18Q125 6 140 20Q160 8 180 22Q192 14 200 20V60Z"/></svg>
</section>

<section class="panel tub-front">
  <div class="brand-name">Tullaby j's</div>
  <svg class="cloud" viewBox="0 0 200 60" height="130" preserveAspectRatio="none" aria-hidden="true"><path fill="var(--cloud)" d="M0 60V25Q15 10 30 22Q45 5 65 18Q85 4 105 18Q125 6 140 20Q160 8 180 22Q192 14 200 20V60Z"/></svg>
  <div class="flavour">Strawberry<small>flavor</small></div>
</section>

<section class="panel tub-back">
  <div class="photo" role="img" aria-label="Photo of a strawberry ice cream scoop in a wafer cone"></div>
  <p class="copy top">Made with fresh milk and ripe strawberries, churned slowly in small batches for a smooth, creamy scoop every time you open the tub.</p>
  <svg class="cloud" viewBox="0 0 200 60" height="110" preserveAspectRatio="none" aria-hidden="true"><path fill="var(--cloud)" d="M0 60V25Q15 10 30 22Q45 5 65 18Q85 4 105 18Q125 6 140 20Q160 8 180 22Q192 14 200 20V60Z"/></svg>
  <p class="copy bottom">Keep frozen at -18°C. Once thawed, do not refreeze. Best enjoyed soon.</p>
  <span class="volume">400 ml</span>
</section>

<section class="panel top-sticker">
  <div class="brand-name">Tullaby j's</div>
  <div class="photo" role="img" aria-label="Photo of strawberry ice cream scoops with sauce and a wafer roll"></div>
  <svg class="cloud" viewBox="0 0 200 60" height="105" preserveAspectRatio="none" aria-hidden="true"><path fill="var(--cloud)" d="M0 60V25Q15 10 30 22Q45 5 65 18Q85 4 105 18Q125 6 140 20Q160 8 180 22Q192 14 200 20V60Z"/></svg>
  <div class="badge">100%<br>natural<br>flavor</div>
  <div class="flavour">Strawberry<small>flavor</small></div>
</section>

<section class="panel side-sticker">
  <div class="brand-name">Tullaby j's</div>
  <div class="photo" role="img" aria-label="Photo of strawberry ice cream scoops with sauce"></div>
  <svg class="cloud" viewBox="0 0 200 60" height="55" preserveAspectRatio="none" aria-hidden="true"><path fill="var(--cloud)" d="M0 60V25Q15 10 30 22Q45 5 65 18Q85 4 105 18Q125 6 140 20Q160 8 180 22Q192 14 200 20V60Z"/></svg>
  <div class="badge">100%<br>natural<br>flavor</div>
  <div class="flavour">Strawberry<small>flavor</small></div>
</section>

</body>
</html>
```